Travertine Marketing Postcard

We have brought quality pool building materials to our customers since 2000. We want our current customers and prospects to see concisely in a post card that we have premium/select travertine coping and pavers as well in stock at great prices. We can deliver the same quality product and service to them with the travertine as we have with our ceramic swimming pool tile. We want them to know that they can call us for a quote. We want them to know that in addition to pricing that is more than competitive, we are offering special freight rates and get the product to them in two business days.
Updates

Reason: I need more time to revise and decide.

Industry/Entity Type

Building

Requirements
Must have
• The quality of the product is premium /select. There are 8 colors and the most popular sizes. Even though the product is coming from GA we are offering special freight rates and in some cases can get the product to their project quicker than the local supplier. Orders received by 2:00PM EST can be shipped same day and received in two days. Outstanding customer service.

```html
<!DOCTYPE html>
<html lang="en">
<head>
<meta charset="utf-8">
<title>Harbor Stone Supply – Travertine Postcard</title>
<link rel="stylesheet" href="https://fonts.googleapis.com/css2?family=Roboto+Condensed:wght@700&display=swap">
<style>
  :root {
    --ink: #4a87ae;
    --ink-deep: #3b5d98;
    --brand: #275a90;
    --rule: #6a79aa;
    --frame: #111111;
    --paper: #ffffff;
    --haze: #d9dcef;
  }
  * { margin: 0; padding: 0; box-sizing: border-box; }
  html, body { width: 1200px; height: 938px; overflow: hidden; background: var(--paper); }
  .postcard {
    position: relative;
    width: 1200px;
    height: 938px;
    background: var(--paper);
    font-family: "Roboto Condensed", "Arial Narrow", sans-serif;
    font-weight: 700;
    color: var(--ink);
    overflow: hidden;
  }
  .backdrop-sweep { position: absolute; left: 800px; top: 80px; width: 400px; height: 830px; }
  .brand-name {
    position: absolute;
    left: 30px; top: 110px;
    width: 352px;
    font-size: 54px;
    line-height: 1.1;
    color: var(--brand);
  }
  .contact { position: absolute; left: 424px; top: 40px; font-size: 35.5px; line-height: 44px; }
  .contact .address { margin-top: 40px; }
  .stamp-box {
    position: absolute;
    left: 926px; top: 42px;
    width: 233px; height: 243px;
    border: 3px solid var(--frame);
  }
  .selling-points { position: absolute; left: 30px; top: 384px; width: 580px; }
  .headline { font-size: 48px; line-height: 56px; margin-bottom: 21px; }
  .point { font-size: 37px; line-height: 47px; margin-bottom: 4px; }
  .accent { color: var(--ink-deep); }
  .address-lines { position: absolute; left: 626px; top: 407px; width: 540px; }
  .address-lines span {
    display: block;
    height: 3px;
    background: var(--rule);
    margin-bottom: 57px;
  }
</style>
</head>
<body>
<div class="postcard">
  <svg class="backdrop-sweep" viewBox="0 0 400 830" role="img" aria-label="Soft lavender lattice sweep decoration">
    <defs>
      <linearGradient id="sweep" x1="0" y1="0" x2="0" y2="1">
        <stop offset="0" stop-color="#d9dcef" stop-opacity="0.15"/>
        <stop offset="0.5" stop-color="#d9dcef" stop-opacity="0.7"/>
        <stop offset="1" stop-color="#d9dcef" stop-opacity="0.1"/>
      </linearGradient>
    </defs>
    <path d="M230 0 C 260 200, 240 420, 20 810 L 400 830 L 400 0 Z" fill="url(#sweep)"/>
  </svg>

  <div class="brand-name">Harbor Stone Supply</div>

  <div class="contact">
    <p class="phone">Phone: 555-014-2276</p>
    <p class="email">Email: info@harborstone.com</p>
    <div class="address">
      <p>1420 Quarry Ridge Ct.</p>
      <p>Dalton, GA&nbsp;&nbsp;30721</p>
    </div>
  </div>

  <div class="stamp-box"></div>

  <div class="selling-points">
    <h1 class="headline">Premium travertine coping</h1>
    <p class="point">and pavers in 8 colors and the<br>most popular sizes</p>
    <p class="point">Special freight rates</p>
    <p class="point">Receive your order in 2 days</p>
    <p class="point">Orders received before 2 PM EST<br>are <span class="accent">shipped the same day</span></p>
    <p class="point accent">Call us today for a quote</p>
  </div>

  <div class="address-lines">
    <span></span><span></span><span></span><span></span><span></span><span></span><span></span>
  </div>
</div>
</body>
</html>
```